Re-design Company presentation for LumoVerityNet

The current presentation has the right content, but we need to make serious changes in terms of colors, backgrounds, etc.
You can view the current state of the PPT as a skeleton that needs to be revamped to make it look professional & visually appealing.
Please feel free to make any changes as necessary, but please maintain text editable and consider that we might add for example new individual client logos in the future, so generally avoid large chunks of images combined together.
If you require any specific logos in a better format, or if you have any questions at all, please feel free to ask.

```html
<!DOCTYPE html>
<html lang="en">
<head>
<meta charset="utf-8">
<title>LumoVerityNet – Company Presentation</title>
<link href="https://fonts.googleapis.com/css2?family=IBM+Plex+Sans:wght@300;400;500&family=Roboto:wght@300;400;500;700&display=swap" rel="stylesheet">
<style>
:root{
  --canvas:#9c9da0;
  --ink:#0b0b0c;
  --white:#ffffff;
  --card:#f4f3f5;
  --blue:#0aa4e8;
  --blue-soft:#cfe9f8;
  --grey-text:#5b5b60;
  --body-text:#46464b;
  --stripe:#8e8e92;
  --pink:#e0345f;
  --teal:#2ab0a8;
  --yellow:#f7c534;
  --pill:#efeff1;
}
*{box-sizing:border-box;margin:0;padding:0}
html,body{width:1200px;height:4415px;overflow:hidden;background:var(--canvas)}
body{position:relative;font-family:"Roboto",Arial,sans-serif;color:var(--ink)}
.slide{position:absolute;left:146px;width:913px;height:646px;background:var(--white);overflow:hidden}
.abs{position:absolute}

/* brand mark */
.brand{position:absolute;display:flex;align-items:center;gap:10px;font-family:"IBM Plex Sans",Arial,sans-serif;color:var(--white)}
.brand-square{background:var(--white);display:block}

/* cover */
.cover{background:var(--ink)}
.cover-title{left:51px;top:364px;font-family:"IBM Plex Sans",Arial,sans-serif;font-weight:400;font-size:41px;line-height:62px;color:var(--white)}
.cover-sub{left:54px;top:498px;font-family:"IBM Plex Sans",Arial,sans-serif;font-weight:300;font-size:19px;line-height:31px;color:var(--white)}

/* section header band */
.band{position:absolute;left:0;top:0;width:913px;height:129px;background:var(--ink)}
.band .brand{left:24px;top:18px;flex-direction:column;gap:8px;font-size:18px}
.band-divider{position:absolute;left:168px;top:20px;width:2px;height:92px;background:var(--white)}
.band-title{position:absolute;left:206px;top:44px;font-size:31px;font-weight:500;color:var(--white)}
.band-stripes{position:absolute;right:0;top:0}

/* clients */
.clients-band{position:absolute;left:0;top:0;width:913px;height:278px;background:radial-gradient(ellipse at 50% 120%,#3a3a3e 0%,#151517 45%,#0b0b0c 75%)}
.clients-title{position:absolute;left:0;width:913px;top:212px;text-align:center;font-size:31px;font-weight:500;color:var(--white)}
.client-grid{position:absolute;left:27px;top:327px;width:862px;display:grid;grid-template-columns:repeat(4,204px);grid-auto-rows:126px;gap:17px 15px}
.client{border:1.5px solid #cfcfd2;display:flex;align-items:center;justify-content:center;gap:8px;font-size:20px;font-weight:500}
.client .dot{width:14px;height:14px;border-radius:50%}
.client .sq{width:14px;height:14px}

/* services */
.service{position:absolute;width:426px;height:208px;background:var(--card)}
.service .icon{position:absolute;left:31px;top:63px;width:82px;height:82px;background:var(--blue);border-radius:10px;transform:rotate(45deg)}
.service .icon svg{position:absolute;left:21px;top:21px;transform:rotate(-45deg)}
.service h3{position:absolute;left:161px;top:26px;font-size:15px;font-weight:700}
.service p{position:absolute;left:161px;top:54px;width:240px;font-size:12.5px;line-height:19px;color:var(--body-text)}

/* stats */
.band-sub{position:absolute;left:211px;top:80px;font-size:12px;line-height:16px;color:var(--white);width:420px}
.stat{position:absolute;top:271px;width:257px;height:330px;background:linear-gradient(#f4f3f5,#ffffff 95%);border-radius:6px}
.stat-back{position:absolute;width:158px;height:158px;background:var(--blue-soft);transform:rotate(45deg);border-radius:8px}
.stat-front{position:absolute;width:158px;height:158px;background:var(--blue);transform:rotate(45deg);border-radius:8px}
.stat-num{position:absolute;width:200px;text-align:center;font-size:48px;font-weight:500;color:var(--white)}
.stat-text{position:absolute;top:420px;width:220px;text-align:center;font-size:18px;line-height:26px;color:var(--grey-text)}

/* differentiators */
.diff-photo{position:absolute;left:12px;top:150px;width:480px;height:480px;clip-path:polygon(50% 0,100% 50%,50% 100%,0 50%);background:linear-gradient(135deg,#5a3b22 0%,#b07a4c 30%,#ececef 55%,#7fb3d9 80%,#dfe6ee 100%)}
.point{position:absolute;display:flex;align-items:center;gap:14px;font-size:16px;height:40px;padding:0 18px 0 0;color:#1b1b1e}
.point::before{content:"";width:10px;height:10px;border-radius:50%;background:#1b1b1e}
.point.pill{background:var(--pill);padding-left:12px;margin-left:-12px}

/* steps */
.step-h{position:absolute;font-size:24px;font-weight:500}
.step-p{position:absolute;font-size:16px;line-height:24px;color:var(--grey-text);font-weight:300}
.step-rule{position:absolute;right:0;height:2px;background:#2a2a2d}
.ring{position:absolute;width:130px;height:130px;border-radius:50%;background:var(--white);box-shadow:0 6px 14px rgba(0,0,0,.2)}
.ring .core{position:absolute;left:17px;top:17px;width:96px;height:96px;border-radius:50%;display:flex;align-items:center;justify-content:center;box-shadow:inset 0 0 0 4px rgba(0,0,0,.08)}
</style>
</head>
<body>

<!-- Slide 1: cover -->
<section class="slide cover" style="top:108px">
  <svg class="abs" style="left:0;top:0" width="913" height="646" viewBox="0 0 913 646">
    <polygon points="720,0 913,0 913,200" fill="#ffffff"/>
    <polygon points="600,646 913,646 913,410" fill="#ffffff"/>
    <g stroke="#0b0b0c" stroke-width="13" stroke-linecap="butt">
      <line x1="715" y1="95" x2="790" y2="20"/>
      <line x1="740" y1="120" x2="815" y2="45"/>
      <line x1="765" y1="145" x2="840" y2="70"/>
      <line x1="790" y1="170" x2="865" y2="95"/>
      <line x1="815" y1="195" x2="890" y2="120"/>
    </g>
  </svg>
  <div class="abs" role="img" aria-label="Photo of hands reviewing analytics charts on a laptop and printed reports"
       style="left:279px;top:-9px;width:658px;height:658px;clip-path:polygon(50% 0,100% 50%,50% 100%,0 50%);background:linear-gradient(135deg,#d9dde3 0%,#9fb4cc 35%,#c9d3df 55%,#b98e6c 80%,#e6e8ec 100%)"></div>
  <div class="brand" style="left:55px;top:60px;flex-direction:column;gap:18px;font-size:30px">
    <span class="brand-square" style="width:78px;height:78px"></span>
    <span>LumoVerityNet</span>
  </div>
  <h1 class="abs cover-title">Tagging Data<br>You Can Trust</h1>
  <p class="abs cover-sub">Proposal Created for {Company} by<br>Ilan Varga &amp; Tomas Rell {Date}</p>
</section>

<!-- Slide 2: clients -->
<section class="slide" style="top:816px">
  <div class="clients-band"></div>
  <div class="brand" style="left:0;width:913px;top:30px;flex-direction:column;gap:16px;font-size:30px">
    <span class="brand-square" style="width:72px;height:72px"></span>
    <span>LumoVerityNet</span>
  </div>
  <h2 class="clients-title">Clients We Work With</h2>
  <div class="client-grid">
    <div class="client" style="color:#22a35a"><span class="dot" style="background:#22a35a"></span>Brightpath</div>
    <div class="client" style="color:#1d2d6b">Norvale</div>
    <div class="client" style="color:#111">Ledgerline</div>
    <div class="client" style="color:#555;font-weight:400;letter-spacing:2px;font-size:17px">QUIETSTAY</div>
    <div class="client" style="color:#1b6fcf"><span class="dot" style="background:#1b6fcf"></span>Atlas Routes</div>
    <div class="client" style="color:#111;font-weight:700">Keelbrook</div>
    <div class="client" style="color:#1d2d6b"><span class="sq" style="background:#e03a8a"></span>MERIDEX</div>
    <div class="client" style="color:#222">Orbitwell</div>
  </div>
</section>

<!-- Slide 3: services -->
<section class="slide" style="top:1524px">
  <div class="band">
    <div class="brand"><span class="brand-square" style="width:46px;height:46px"></span><span>LumoVerityNet</span></div>
    <div class="band-divider"></div>
    <h2 class="band-title">Our Services</h2>
    <svg class="band-stripes" width="300" height="129" viewBox="0 0 300 129"><g stroke="#8e8e92" stroke-width="18"><line x1="10" y1="140" x2="90" y2="10"/><line x1="60" y1="140" x2="140" y2="10"/><line x1="110" y1="140" x2="190" y2="10"/><line x1="160" y1="140" x2="240" y2="10"/></g></svg>
  </div>
  <article class="service" style="left:22px;top:163px">
    <div class="icon"><svg width="40" height="40" viewBox="0 0 40 40" fill="none" stroke="#fff" stroke-width="3"><circle cx="20" cy="20" r="7"/><circle cx="20" cy="20" r="15" stroke-dasharray="6 4"/></svg></div>
    <h3>Analytics Implementation</h3>
    <p>We help you deploy analytics and measurement capabilities. Providing you with data and tagging expertise to create an effective reporting framework. We are specialists in data compliance, data privacy and consent management</p>
  </article>
  <article class="service" style="left:466px;top:163px">
    <div class="icon"><svg width="40" height="40" viewBox="0 0 40 40" fill="none" stroke="#fff" stroke-width="3"><rect x="9" y="5" width="22" height="30" rx="2"/><line x1="14" y1="14" x2="26" y2="14"/><line x1="14" y1="20" x2="26" y2="20"/><line x1="14" y1="26" x2="22" y2="26"/></svg></div>
    <h3>Data Strategy</h3>
    <p style="top:50px">Starting from requirements gathering &amp; auditing your current set-up, to solution architecture &amp; continuous development plans, our team has the capability to take your project from its idea stages, to a fully-fledged business solution that can be used to expand your business.</p>
  </article>
  <article class="service" style="left:22px;top:393px">
    <div class="icon"><svg width="40" height="40" viewBox="0 0 40 40" fill="none" stroke="#fff" stroke-width="3"><path d="M13 22a9 9 0 1 1 14 0l-2 5H15z"/><line x1="15" y1="32" x2="25" y2="32"/></svg></div>
    <h3>Advanced Technologies</h3>
    <p>We partner with visionary customers who want to transform and grow their organization by building their business using modern digital marketing technologies. We develop custom data models to help you track revenue against marketing spend.</p>
  </article>
  <article class="service" style="left:466px;top:393px">
    <div class="icon"><svg width="40" height="40" viewBox="0 0 40 40" fill="#fff"><path d="M20 4 34 18H25V34H15V18H6z"/></svg></div>
    <h3>Continuous Improvement</h3>
    <p style="top:50px">All our solutions are designed to include multiple fail-safes. Our code &amp; configurations are engineered to be robust and to allow future development. We include automated testing tools that can help our clients maintain high Data Quality standards at all times.</p>
  </article>
</section>

<!-- Slide 4: problems -->
<section class="slide" style="top:2232px">
  <div class="band">
    <div class="brand"><span class="brand-square" style="width:46px;height:46px"></span><span>LumoVerityNet</span></div>
    <div class="band-divider"></div>
    <h2 class="band-title" style="top:26px">Data Related Problems</h2>
    <p class="band-sub">Companies are struggling with data tagging, consent, privacy compliance and the ability to measure return on marketing spend</p>
    <svg class="band-stripes" width="300" height="129" viewBox="0 0 300 129"><g stroke="#8e8e92" stroke-width="18"><line x1="10" y1="140" x2="90" y2="10"/><line x1="60" y1="140" x2="140" y2="10"/><line x1="110" y1="140" x2="190" y2="10"/><line x1="160" y1="140" x2="240" y2="10"/></g></svg>
  </div>
  <div class="stat" style="left:38px"></div>
  <div class="stat" style="left:328px"></div>
  <div class="stat" style="left:626px"></div>

  <div class="stat-back" style="left:88px;top:178px"></div>
  <div class="stat-front" style="left:88px;top:197px"></div>
  <div class="stat-num" style="left:67px;top:245px">85%</div>
  <p class="stat-text" style="left:57px">of business are not fully confident in their consent management and privacy compliance strategy</p>

  <div class="stat-back" style="left:377px;top:178px"></div>
  <div class="stat-front" style="left:377px;top:197px"></div>
  <div class="stat-num" style="left:356px;top:245px">76%</div>
  <p class="stat-text" style="left:346px">of businesses don't understand traffic sources or unable to visualize revenue against marketing sources</p>

  <div class="stat-back" style="left:675px;top:178px"></div>
  <div class="stat-front" style="left:675px;top:197px"></div>
  <div class="stat-num" style="left:654px;top:245px">74%</div>
  <p class="stat-text" style="left:644px;width:220px;padding:0 28px">of businesses don't have a universal data tagging governance in place</p>
</section>

<!-- Slide 5: differentiators -->
<section class="slide" style="top:2940px">
  <div class="band">
    <div class="brand"><span class="brand-square" style="width:46px;height:46px"></span><span>LumoVerityNet</span></div>
    <div class="band-divider"></div>
    <h2 class="band-title">What Makes us different</h2>
    <svg class="band-stripes" width="300" height="129" viewBox="0 0 300 129"><g stroke="#8e8e92" stroke-width="18"><line x1="10" y1="140" x2="90" y2="10"/><line x1="60" y1="140" x2="140" y2="10"/><line x1="110" y1="140" x2="190" y2="10"/><line x1="160" y1="140" x2="240" y2="10"/></g></svg>
  </div>
  <div class="diff-photo" role="img" aria-label="Photo of a hand with a stylus touching a glowing digital network of people icons"></div>
  <ul style="list-style:none">
    <li class="point" style="left:358px;top:166px">Highly experienced consultants</li>
    <li class="point pill" style="left:432px;top:233px">Obsession for delivering flawless data</li>
    <li class="point" style="left:487px;top:300px">Elastic team tailored by project</li>
    <li class="point pill" style="left:534px;top:370px">Platform &amp; technology agnostic</li>
    <li class="point" style="left:473px;top:440px">Experts in delivering Automated QA solutions</li>
    <li class="point pill" style="left:420px;top:515px">Data discrepancy investigation maestros</li>
    <li class="point" style="left:346px;top:577px">Deep expertise in Data Privacy compliance &amp; technology</li>
  </ul>
</section>

<!-- Slide 6: next steps -->
<section class="slide" style="top:3648px">
  <div class="band">
    <div class="brand"><span class="brand-square" style="width:46px;height:46px"></span><span>LumoVerityNet</span></div>
    <div class="band-divider"></div>
    <h2 class="band-title">Next Steps to proceed</h2>
    <svg class="band-stripes" width="300" height="129" viewBox="0 0 300 129"><g stroke="#8e8e92" stroke-width="18"><line x1="10" y1="140" x2="90" y2="10"/><line x1="60" y1="140" x2="140" y2="10"/><line x1="110" y1="140" x2="190" y2="10"/><line x1="160" y1="140" x2="240" y2="10"/></g></svg>
  </div>
  <div class="abs" style="left:394px;top:129px;width:12px;height:160px;background:var(--pink)"></div>
  <div class="abs" style="left:221px;top:359px;width:130px;height:12px;background:var(--teal)"></div>
  <div class="abs" style="left:111px;top:479px;width:120px;height:12px;background:var(--yellow)"></div>
  <div class="step-rule" style="left:409px;top:392px"></div>
  <div class="step-rule" style="left:300px;top:526px"></div>

  <div class="ring" style="left:278px;top:243px"><div class="core" style="background:var(--pink)">
    <svg width="46" height="46" viewBox="0 0 46 46" fill="none" stroke="#fff" stroke-width="4" stroke-linecap="round"><path d="M23 40V14M23 6l-6 8h12z" fill="#fff"/><path d="M23 26 10 14M23 26l13-12"/></svg>
  </div></div>
  <div class="ring" style="left:156px;top:362px"><div class="core" style="background:var(--teal)">
    <svg width="40" height="44" viewBox="0 0 40 44" fill="none" stroke="#fff" stroke-width="3.5"><rect x="5" y="4" width="26" height="36" rx="2"/><line x1="11" y1="14" x2="25" y2="14"/><line x1="11" y1="22" x2="25" y2="22"/><line x1="11" y1="30" x2="19" y2="30"/></svg>
  </div></div>
  <div class="ring" style="left:46px;top:482px"><div class="core" style="background:var(--yellow)">
    <svg width="44" height="44" viewBox="0 0 44 44" fill="#fff"><path d="M38 6C26 6 16 14 13 26l5 5C30 28 38 18 38 6z"/><path d="M12 30l-6 8 8-6z"/></svg>
  </div></div>

  <h3 class="step-h" style="left:442px;top:254px">Decision</h3>
  <p class="step-p" style="left:442px;top:292px">let us know when you would like to start, or if you<br>require any further clarifications</p>
  <h3 class="step-h" style="left:340px;top:410px">Contract</h3>
  <p class="step-p" style="left:340px;top:446px">discussion over commercial terms to seal the deal officially</p>
  <h3 class="step-h" style="left:219px;top:533px">Start</h3>
  <p class="step-p" style="left:219px;top:572px">sort out access &amp; begin the project</p>
</section>

</body>
</html>
```